Business Card

I need a professional business card. I would like the front to read:
Morgan Tull
Designated Pilot Examiner
321-555-0187
info@dpemorgan.example
www.dpemorgan.example

I would like the back to be matte black with a glossy black raised image of the lines from a VFR sectional chart of the local airspace in west palm. can be found at www.aerolumen.example

Attached picture is my previous card and sectional chart I would like into lines for the back.

```html
<!DOCTYPE html>
<html lang="en">
<head>
<meta charset="utf-8">
<title>Morgan Tull – Business Card</title>
<link rel="stylesheet" href="https://fonts.googleapis.com/css2?family=Poppins:wght@400;500;700;800&display=swap">
<style>
  :root{
    --stage:#2e2e2e;
    --ink:#111111;
    --paper:#ffffff;
    --rule:#6b6b6b;
    --chart-sky:#c9e6ef;
    --chart-land:#e9f2d8;
    --chart-city:#f3ef6a;
  }
  *{margin:0;padding:0;box-sizing:border-box}
  html,body{width:1200px;height:689px;overflow:hidden}
  body{background:var(--stage);font-family:"Poppins",sans-serif;position:relative}
  .card{position:absolute;top:190px;width:540px;height:309px;border-radius:18px;overflow:hidden}
  .card--back{left:40px}
  .card--front{left:620px;background:var(--paper)}
  .chart-art{position:absolute;inset:0;
    background:linear-gradient(120deg,var(--chart-land) 0%,var(--chart-city) 38%,var(--chart-city) 52%,var(--chart-sky) 70%,var(--chart-sky) 100%)}
  .front-shapes{position:absolute;inset:0}
  .aircraft-art{position:absolute;left:330px;top:30px;width:180px;height:110px;background:var(--ink);border-radius:10px}
  .divider{position:absolute;left:250px;right:24px;top:150px;height:1px;background:var(--rule)}
  .identity{position:absolute;left:92px;top:160px;color:var(--ink)}
  .identity__name{font-weight:800;font-size:24px;letter-spacing:.5px;line-height:1.05;text-transform:uppercase}
  .identity__title{font-weight:400;font-size:15px;line-height:1.3}
  .identity__rule{width:230px;height:1px;background:var(--rule);margin:6px 0 7px}
  .contact{list-style:none}
  .contact li{display:flex;align-items:center;gap:8px;font-size:14px;line-height:1.5}
  .contact svg{width:15px;height:15px;flex:none}
</style>
</head>
<body>
  <section class="card card--back">
    <div class="chart-art" role="img" aria-label="VFR sectional chart of the West Palm Beach airspace"></div>
  </section>

  <section class="card card--front">
    <svg class="front-shapes" viewBox="0 0 540 309" aria-hidden="true">
      <path d="M0 0 H330 C240 30 120 60 70 150 C52 190 46 250 44 309 H0 Z" fill="var(--ink)"/>
      <path d="M200 52 C130 80 78 130 54 230 C82 140 130 98 222 48 Z" fill="var(--paper)"/>
    </svg>
    <div class="aircraft-art" role="img" aria-label="Silhouette of a high-wing light aircraft in flight"></div>
    <div class="divider"></div>
    <div class="identity">
      <h1 class="identity__name">Morgan Tull</h1>
      <p class="identity__title">Designated Pilot Examiner</p>
      <div class="identity__rule"></div>
      <ul class="contact">
        <li><svg viewBox="0 0 16 16"><circle cx="8" cy="8" r="7.3" fill="none" stroke="#111" stroke-width="1"/><path d="M5.5 4.5l1.5 1.2-.6 1.3a5 5 0 0 0 2.6 2.6l1.3-.6 1.2 1.5-1 1c-3 0-6-3-6-6z" fill="#111"/></svg>321-555-0187</li>
        <li><svg viewBox="0 0 16 16"><circle cx="8" cy="8" r="7.3" fill="none" stroke="#111" stroke-width="1"/><rect x="4" y="5.3" width="8" height="5.4" fill="#111"/><path d="M4 5.3l4 3 4-3" fill="none" stroke="#fff" stroke-width=".8"/></svg>info@dpemorgan.example</li>
        <li><svg viewBox="0 0 16 16"><circle cx="8" cy="8" r="7.3" fill="none" stroke="#111" stroke-width="1"/><circle cx="8" cy="8" r="4" fill="none" stroke="#111" stroke-width=".9"/><path d="M4 8h8M8 4c-2 2.2-2 5.8 0 8M8 4c2 2.2 2 5.8 0 8" fill="none" stroke="#111" stroke-width=".8"/></svg>www.dpemorgan.example</li>
      </ul>
    </div>
  </section>
</body>
</html>
```